Used Car Dealer seeks an Amazing Business Card Design

We are looking for a business card design that incorporates our logo and grabs the attention of anyone we give the business card to.

Looking to use the same colors as the logo. Our Logo choice is the black background with Red and Silver/Grey Lettering.

We also would like to see some embossed designs.

Target Market(s)

Used Car Buyers, Automotive, Auto

Industry/Entity Type

Automotive

Contact Information for Business Card

BVEL7K
Gordon Whitlock
482 Tarrow Lane
Suite 207
Roswell, GA 30075
Office (770) 555-0142
Cell (770) 555-0187
bvel7kga@quellmail.com
www.bvel7kga.com

Colors
ffffff
ee3036

Requirements
Must have
• Must include our logo (Black Background with Red and Silver/Grey Lettering)
Nice to have
• Embossed Design. Can be Single or Double Sided.

```html
<!DOCTYPE html>
<html lang="en">
<head>
<meta charset="utf-8">
<title>BVEL7K Business Card</title>
<link href="https://fonts.googleapis.com/css2?family=Lato:wght@400;700&family=Montserrat:wght@800&display=swap" rel="stylesheet">
<style>
  :root {
    --backdrop: #2a2b2d;
    --card: #1c1e20;
    --card-edge: #25282a;
    --red: #ee3036;
    --white: #ffffff;
  }
  * { box-sizing: border-box; margin: 0; padding: 0; }
  html, body {
    width: 1200px; height: 1189px; overflow: hidden;
    background: radial-gradient(ellipse at 40% 30%, #3a3b3d 0%, var(--backdrop) 55%, #161718 100%);
    font-family: "Lato", sans-serif;
  }
  .stage {
    position: relative; width: 1200px; height: 1189px;
    display: flex; flex-direction: column; align-items: center; justify-content: center; gap: 70px;
  }
  .card {
    position: relative; width: 860px; height: 491px;
    background: linear-gradient(160deg, var(--card-edge), var(--card));
    border-radius: 30px;
    box-shadow: 0 18px 40px rgba(0,0,0,.55);
  }
  .brand-name {
    font-family: "Lato", sans-serif; font-weight: 700;
    color: var(--red); letter-spacing: 2px; line-height: 1;
  }
  .card-front { display: flex; align-items: center; justify-content: center; }
  .card-front .brand-name { font-size: 104px; }

  .card-back { display: flex; align-items: center; }
  .card-back .brand-block { width: 475px; display: flex; justify-content: center; }
  .card-back .brand-name { font-size: 78px; }
  .divider {
    position: absolute; left: 475px; top: 95px; width: 2px; height: 300px; background: var(--red);
  }
  .details { position: absolute; left: 510px; top: 100px; right: 24px; color: var(--white); }
  .person-name {
    font-family: "Montserrat", sans-serif; font-weight: 800; font-size: 26px; letter-spacing: 1px;
    white-space: nowrap;
  }
  .person-role { color: var(--red); font-size: 21px; margin-top: 2px; }
  .address { margin-top: 22px; margin-left: 30px; font-size: 21px; line-height: 1.3; }
  .contact-list { list-style: none; margin-top: 12px; margin-left: 30px; }
  .contact-list li {
    display: flex; align-items: center; gap: 10px; font-size: 21px; line-height: 1.4; white-space: nowrap;
  }
  .contact-icon {
    width: 22px; height: 22px; border-radius: 5px; background: var(--red);
    display: flex; align-items: center; justify-content: center; flex-shrink: 0;
  }
  .contact-icon svg { width: 14px; height: 14px; fill: none; stroke: var(--white); stroke-width: 2; }
</style>
</head>
<body>
<main class="stage">
  <section class="card card-front">
    <span class="brand-name">BVEL7K</span>
  </section>

  <section class="card card-back">
    <div class="brand-block"><span class="brand-name">BVEL7K</span></div>
    <div class="divider"></div>
    <div class="details">
      <p class="person-name">GORDON WHITLOCK</p>
      <p class="person-role">Director</p>
      <p class="address">482 Tarrow Lane, Suite 207<br>Roswell, GA 30075</p>
      <ul class="contact-list">
        <li><span class="contact-icon"><svg viewBox="0 0 16 16"><path d="M4 2l3 3-1.5 1.5a8 8 0 0 0 4 4L11 9l3 3-2 2C7 14 2 9 2 4z" fill="#fff" stroke="none"/></svg></span>(770) 555-0142</li>
        <li><span class="contact-icon"><svg viewBox="0 0 16 16"><rect x="4" y="1.5" width="8" height="13" rx="1.5"/><line x1="7" y1="12" x2="9" y2="12"/></svg></span>(770) 555-0187</li>
        <li><span class="contact-icon"><svg viewBox="0 0 16 16"><rect x="1.5" y="3.5" width="13" height="9"/><polyline points="1.5,3.5 8,9 14.5,3.5"/></svg></span>bvel7kga@quellmail.com</li>
        <li><span class="contact-icon"><svg viewBox="0 0 16 16"><circle cx="8" cy="8" r="6"/><ellipse cx="8" cy="8" rx="2.5" ry="6"/><line x1="2" y1="8" x2="14" y2="8"/></svg></span>www.bvel7kga.com</li>
      </ul>
    </div>
  </section>
</main>
</body>
</html>
```